Business Card for New Business

Please design a business card using our logo and font files. This is only one card for one person, as listed in details section.

Industry/Entity Type

Business

Contact Information for Business Card

Carl Voserby

Phone 240.318.6624
Cell 703.581.4096
Email carl@moltravex.com

www.moltravex.com

Address
18250 Brennick Lane #314
Damascus, MD 20715

Font styles to use
Sans Serif

Requirements
Must have
• Information listed in detail section. Must be standard card size.

```html
<!DOCTYPE html>
<html lang="en">
<head>
<meta charset="utf-8">
<title>Moltravex – Business Card</title>
<link href="https://fonts.googleapis.com/css2?family=Questrial&display=swap" rel="stylesheet">
<style>
  :root {
    --page-bg: #e6e6e6;
    --card-bg: #ffffff;
    --brand-red: #d6281e;
    --brand-orange: #e85a1f;
    --ink: #333333;
  }
  html, body {
    margin: 0;
    padding: 0;
    width: 1200px;
    height: 900px;
    overflow: hidden;
    background: var(--page-bg);
    font-family: "Questrial", "Century Gothic", sans-serif;
  }
  .card {
    position: absolute;
    left: 150px;
    top: 193px;
    width: 900px;
    height: 514px;
    background: var(--card-bg);
    border-radius: 34px;
    box-shadow: 0 6px 24px rgba(0,0,0,0.12);
    overflow: hidden;
  }
  .company-name {
    position: absolute;
    right: 70px;
    top: 74px;
    margin: 0;
    font-size: 40px;
    font-weight: 400;
    line-height: 1;
    color: var(--ink);
    letter-spacing: 1px;
  }
  .divider-long {
    position: absolute;
    left: 380px;
    right: 60px;
    top: 292px;
    height: 1.5px;
    background: var(--brand-orange);
  }
  .address {
    position: absolute;
    right: 60px;
    top: 310px;
    text-align: right;
    font-size: 17px;
    line-height: 1.45;
    letter-spacing: 1.2px;
    color: var(--ink);
  }
  .address .web {
    color: var(--brand-red);
    font-weight: 700;
    letter-spacing: 1.5px;
  }
  .person {
    position: absolute;
    left: 70px;
    top: 248px;
  }
  .person-name {
    font-size: 40px;
    line-height: 1;
    color: var(--brand-red);
    letter-spacing: 1px;
  }
  .person-title {
    margin-top: 6px;
    font-size: 18px;
    color: var(--ink);
    letter-spacing: 1.5px;
  }
  .divider-short {
    width: 270px;
    height: 1.5px;
    margin-top: 10px;
    background: var(--brand-red);
  }
  .contacts {
    list-style: none;
    margin: 14px 0 0 0;
    padding: 0;
  }
  .contacts li {
    display: flex;
    align-items: center;
    gap: 16px;
    font-size: 17px;
    line-height: 30px;
    letter-spacing: 1.5px;
    color: var(--ink);
  }
  .contacts svg {
    width: 18px;
    height: 18px;
    fill: none;
    stroke: var(--brand-red);
    stroke-width: 2;
  }
  .contacts svg .solid { fill: var(--brand-red); stroke: none; }
</style>
</head>
<body>
  <div class="card">
    <p class="company-name">Moltravex</p>

    <div class="divider-long"></div>

    <div class="address">
      18250 Brennick Lane #314<br>
      Damascus, MD 20715<br>
      <span class="web">www.moltravex.com</span>
    </div>

    <div class="person">
      <div class="person-name">Carl Voserby</div>
      <div class="person-title">Managing Director</div>
      <div class="divider-short"></div>
      <ul class="contacts">
        <li>
          <svg viewBox="0 0 24 24" aria-label="Phone"><path class="solid" d="M6.6 10.8a15 15 0 0 0 6.6 6.6l2.2-2.2a1 1 0 0 1 1-.25 11.4 11.4 0 0 0 3.6.6 1 1 0 0 1 1 1V20a1 1 0 0 1-1 1A17 17 0 0 1 3 4a1 1 0 0 1 1-1h3.5a1 1 0 0 1 1 1c0 1.25.2 2.45.6 3.6a1 1 0 0 1-.25 1z"/></svg>
          <span>240.318.6624</span>
        </li>
        <li>
          <svg viewBox="0 0 24 24" aria-label="Cell"><rect x="7" y="2" width="10" height="20" rx="2"/><line x1="11" y1="18" x2="13" y2="18"/></svg>
          <span>703.581.4096</span>
        </li>
        <li>
          <svg viewBox="0 0 24 24" aria-label="Email"><rect x="3" y="5" width="18" height="14"/><polyline points="3,5 12,13 21,5"/></svg>
          <span>carl@moltravex.com</span>
        </li>
      </ul>
    </div>
  </div>
</body>
</html>
```